"Oral Surgery Office needs a Business Card Design with Logo"

We need a logo design and business card. The name of the office is Halvering Oral Surgery & Implant Center. The final design should communicate uniqueness as well as highly class office. The business card should emphasize power. I included the current business card below. Please design something unique

Target Market(s)

Dentists & Patients

Industry/Entity Type

Dental

Contact Information for Business Card

Unique Design to show success, prestige, Style, unmatched performance

Font styles to use
Serif

Colors
1b1b1b
ffffff
0556a4

Requirements
Must have
• Bussiness Name, Doctor's Name, Website, phone and Fax, email, office address
• Color should be either Black and White or Blue and White
Nice to have
• Clean look
Should not have
• the business card shouldn't be too busy. I feel like the old business card was too busy

```html
<!DOCTYPE html>
<html lang="en">
<head>
<meta charset="utf-8">
<title>Halvering Oral Surgery &amp; Implant Center – Business Card</title>
<link rel="stylesheet" href="https://fonts.googleapis.com/css2?family=Open+Sans:wght@400;600;700&display=swap">
<style>
  :root {
    --ink: #1b1b1b;
    --blue: #1877bf;
    --paper: #ffffff;
    --backdrop: #e4e6e8;
    --mark: #2a2a2a;
  }
  * { box-sizing: border-box; margin: 0; padding: 0; }
  html, body {
    width: 1200px;
    height: 970px;
    overflow: hidden;
    background: var(--backdrop);
  }
  .stage {
    position: relative;
    width: 1200px;
    height: 970px;
  }
  .card {
    position: absolute;
    left: 100px;
    top: 207px;
    width: 1000px;
    height: 556px;
    background: var(--paper);
    box-shadow: 0 6px 24px rgba(0,0,0,0.12);
    font-family: "Open Sans", Arial, sans-serif;
    color: var(--ink);
    overflow: hidden;
  }
  .brand {
    position: absolute;
    left: 48px;
    top: 45px;
    display: flex;
    align-items: center;
    gap: 26px;
  }
  .brand-square {
    width: 150px;
    height: 150px;
    background: var(--mark);
  }
  .brand-name {
    font-weight: 700;
    font-size: 33px;
    line-height: 1.35;
    letter-spacing: 0.5px;
    text-transform: uppercase;
    color: var(--ink);
  }
  .brand-name span { display: block; }
  .doctor {
    position: absolute;
    right: 47px;
    top: 272px;
    text-align: right;
  }
  .doctor-name {
    font-size: 29px;
    font-weight: 700;
    line-height: 40px;
  }
  .doctor-name .degree { font-weight: 400; }
  .doctor-specialty {
    font-size: 23px;
    color: var(--blue);
    line-height: 32px;
  }
  .contact {
    position: absolute;
    left: 48px;
    top: 308px;
    list-style: none;
    font-size: 24px;
    line-height: 33px;
  }
  .contact li {
    display: flex;
    align-items: center;
    gap: 10px;
  }
  .contact svg { width: 24px; height: 20px; fill: var(--ink); flex: none; }
  .contact .address { margin-top: 7px; }
  .footer-bands {
    position: absolute;
    left: 0;
    bottom: 0;
    width: 1000px;
    height: 45px;
  }
  .footer-bands .band-dark { fill: var(--ink); }
  .footer-bands .band-blue { fill: var(--blue); }
</style>
</head>
<body>
<main class="stage">
  <section class="card">
    <header class="brand">
      <div class="brand-square"></div>
      <h1 class="brand-name"><span>Halvering Oral Surgery</span><span>&amp; Implant Center</span></h1>
    </header>

    <div class="doctor">
      <p class="doctor-name">Dr. Miriam Castellane<span class="degree">, D.D.S</span></p>
      <p class="doctor-specialty">Oral &amp; Maxillofacial Surgery</p>
    </div>

    <ul class="contact">
      <li>
        <svg viewBox="0 0 24 20" aria-hidden="true"><path d="M2 6c0-3 4-4 10-4s10 1 10 4v2h-5V6H7v2H2z"/><path d="M6 9h12l3 9H3z"/></svg>
        555 - 214 - 3870
      </li>
      <li>
        <svg viewBox="0 0 24 20" aria-hidden="true"><rect x="6" y="1" width="12" height="5"/><rect x="1" y="7" width="22" height="8" rx="1"/><rect x="6" y="13" width="12" height="6"/></svg>
        555 - 214 - 3871
      </li>
      <li>
        <svg viewBox="0 0 24 20" aria-hidden="true"><path d="M2 4h20v12H2z M3 5l9 6 9-6" fill="none" stroke="#1b1b1b" stroke-width="2"/></svg>
        halveringoralsurgery@mail.com
      </li>
      <li>
        <svg viewBox="0 0 24 20" aria-hidden="true"><rect x="2" y="2" width="20" height="12" fill="none" stroke="#1b1b1b" stroke-width="2"/><rect x="8" y="16" width="8" height="2"/></svg>
        www.halveringoralsurgery.com
      </li>
      <li class="address">2480 Larkmoor Avenue, Halvering, NY 11960</li>
    </ul>

    <svg class="footer-bands" viewBox="0 0 1000 45" aria-hidden="true">
      <polygon class="band-dark" points="0,0 592,0 650,45 0,45"/>
      <polygon class="band-blue" points="628,13 1000,13 1000,45 668,45"/>
    </svg>
  </section>
</main>
</body>
</html>
```